Metal Recycling Website Require New Design for upgrade

Our company currently have an existing website, www.tovarekmetals.com and the website is generally outdated so we would like an improvement.

We would generally prefer to keep the current color theme of our website as it is similar to our current logo.

We would also like our company factory picture to be on somewhere of the webpage (but only if the designer think that the picture can blend well with the color theme)

Our company is dealing alot Aluminiun, Stainless Steel, Copper, Brass, Iron

Pictures uploaded.

Target Market(s)

General Commercial Manufacturer, B2B

Industry/Entity Type

Recycling

Number of Pages Required

1 page

Colors

Designer to choose colors to be used in the design.

Requirements
Must have
• Hopefully color will be similar to my logo theme but designer welcome to have their own input.
Nice to have
• Company Picture (Uploaded in the file)

```html
<!DOCTYPE html>
<html lang="en">
<head>
<meta charset="utf-8">
<title>Tovarek Metals Recycling</title>
<link href="https://fonts.googleapis.com/css2?family=Montserrat:wght@400;600;700;800&family=Open+Sans:wght@400;600&display=swap" rel="stylesheet">
<style>
:root{
  --gold:#e2a31f;
  --dark:#141414;
  --dark-2:#1f1f1f;
  --ink:#2b2b2b;
  --muted:#7a7a7a;
  --light:#f2f2f2;
  --line:#e2e2e2;
  --white:#ffffff;
}
*{box-sizing:border-box;margin:0;padding:0}
html,body{width:1200px;height:3028px;overflow:hidden}
body{font-family:"Open Sans",Arial,sans-serif;color:var(--ink);background:var(--white);font-size:14px;line-height:1.6}
h1,h2,h3,h4,.brand,.nav a,.btn,.eyebrow{font-family:"Montserrat",Arial,sans-serif}
.wrap{width:1040px;margin:0 auto;position:relative}

/* header */
.site-header{height:112px;background:var(--dark);}
.site-header .wrap{height:112px}
.brand{position:absolute;left:0;top:18px;display:flex;align-items:center;gap:12px;color:var(--gold);font-weight:700;font-size:17px;line-height:1.1;letter-spacing:.5px}
.brand-mark{width:34px;height:34px;border:2px solid var(--gold)}
.contact-strip{position:absolute;right:0;top:24px;display:flex;gap:30px;color:#cfcfcf;font-size:12px}
.contact-strip span{display:flex;align-items:center;gap:7px}
.nav{position:absolute;left:0;top:74px;display:flex;gap:6px}
.nav a{color:#d8d8d8;font-size:12px;font-weight:600;text-decoration:none;padding:8px 14px;text-transform:uppercase}
.nav a.active{background:var(--gold);color:var(--white)}

/* hero */
.hero{height:380px;background:linear-gradient(180deg,#3a3a3a,#555 40%,#2d2d2d);position:relative;text-align:center;color:var(--white)}
.hero-inner{position:absolute;left:0;right:0;top:150px}
.hero h1{font-size:44px;font-weight:800;letter-spacing:1px}
.hero h1 em{color:var(--gold);font-style:normal}
.hero p{font-family:"Montserrat",sans-serif;font-size:14px;font-weight:600;letter-spacing:2px;margin-top:6px}

/* about */
.about{height:500px;background:var(--light)}
.about .wrap{padding-top:100px;display:flex;justify-content:space-between}
.about-text{width:470px}
.eyebrow{color:var(--gold);font-size:11px;font-weight:600;text-transform:uppercase;letter-spacing:1px}
.section-title{font-size:17px;font-weight:700;text-transform:uppercase;color:var(--ink);margin-bottom:16px}
.about-text .lead{font-family:"Montserrat",sans-serif;font-weight:700;font-size:16px;line-height:1.4;margin-bottom:14px}
.about-text p{font-size:12px;color:var(--muted)}
.btn{display:inline-block;background:var(--gold);color:var(--white);font-size:12px;font-weight:600;padding:10px 24px;border-radius:20px;margin-top:24px;text-transform:uppercase}
.factory-photo{width:330px;height:330px;border-radius:50%;background:radial-gradient(circle at 50% 40%,#bcd6e6,#6fa57c 55%,#3d6b4a);margin-right:40px;margin-top:-10px}

/* services */
.services{height:600px}
.services .wrap{padding-top:60px}
.services-head{display:flex;justify-content:space-between;align-items:flex-end;margin-bottom:40px}
.services-head .lead{font-family:"Montserrat",sans-serif;font-weight:700;font-size:15px;width:640px;line-height:1.4}
.services-head .btn{margin-top:0}
.cards{display:flex;justify-content:space-between}
.card{width:300px;background:var(--white);box-shadow:0 4px 16px rgba(0,0,0,.1)}
.card-photo{height:170px}
.card:nth-child(1) .card-photo{background:linear-gradient(135deg,#3b3b3b,#6b6660,#2a2a2a)}
.card:nth-child(2) .card-photo{background:linear-gradient(135deg,#4a4a4a,#7a7a78,#333)}
.card:nth-child(3) .card-photo{background:linear-gradient(135deg,#6b4a2a,#9a7046,#4a3020)}
.card-body{padding:20px 20px 18px}
.card h3{font-size:14px;font-weight:700;margin-bottom:8px}
.card p{font-size:11px;color:var(--muted);line-height:1.55}
.card .more{display:block;text-align:right;color:var(--gold);font-size:11px;font-weight:600;margin-top:12px}

/* process */
.process{height:600px;background:var(--light);text-align:center}
.process .wrap{padding-top:20px}
.process .section-title{margin-bottom:40px}
.steps{display:grid;grid-template-columns:repeat(3,1fr);row-gap:50px;column-gap:60px}
.step svg{width:54px;height:54px}
.step h4{font-size:12px;font-weight:700;text-transform:uppercase;margin:10px 0 6px}
.step p{font-size:11px;color:var(--muted);line-height:1.5;padding:0 20px}

/* contact */
.contact{height:580px}
.contact .wrap{padding-top:30px}
.contact .head{text-align:center;margin-bottom:40px}
.contact-body{display:flex;justify-content:space-between}
.form{width:460px}
.form .note{color:var(--gold);font-size:12px}
.form .note-2{font-family:"Montserrat",sans-serif;font-size:13px;font-weight:700;margin-bottom:16px}
.row{display:flex;gap:20px;margin-bottom:16px}
.field{flex:1;height:40px;border:1px solid var(--line);padding:10px 12px;font-size:11px;color:#aaa}
.field.msg{height:110px}
.form .btn{border-radius:3px;margin-top:4px;padding:9px 24px}
.map{width:520px;height:320px;background:linear-gradient(135deg,#e8ecef,#d6e3d6 50%,#b9d3e9)}

/* footer */
.site-footer{height:268px;background:var(--dark);color:#a9a9a9;font-size:11px}
.site-footer .wrap{padding-top:32px;display:flex;justify-content:space-between}
.foot-col{width:220px}
.foot-col h4{color:var(--white);font-size:12px;font-weight:600;text-transform:uppercase;margin-bottom:14px}
.foot-col .brand{position:static;margin-bottom:16px}
.foot-col li{list-style:none;line-height:1.9}
.copyright{position:absolute;left:0;right:0;bottom:10px;text-align:center;font-size:10px;color:#777;border-top:1px solid #2c2c2c;padding-top:8px}
.site-footer{position:relative}
</style>
</head>
<body>

<header class="site-header">
  <div class="wrap">
    <div class="brand"><span class="brand-mark"></span><span>TOVAREK METALS<br>RECYCLING</span></div>
    <div class="contact-strip">
      <span><svg width="12" height="14" viewBox="0 0 12 14"><path d="M6 0a5 5 0 0 0-5 5c0 4 5 9 5 9s5-5 5-9a5 5 0 0 0-5-5zm0 7a2 2 0 1 1 0-4 2 2 0 0 1 0 4z" fill="#e2a31f"/></svg>18 Harbour Works Lane,<br>Singapore 700018</span>
      <span><svg width="12" height="12" viewBox="0 0 12 12"><path d="M2 0l3 3-1.5 1.5a7 7 0 0 0 4 4L9 7l3 3-2 2C5 12 0 7 0 2z" fill="#e2a31f"/></svg>+65 6100 2040</span>
      <span><svg width="14" height="10" viewBox="0 0 14 10"><rect x=".5" y=".5" width="13" height="9" fill="none" stroke="#e2a31f"/><path d="M.5.5 7 6l6.5-5.5" fill="none" stroke="#e2a31f"/></svg>hello@tovarekmetals.com</span>
    </div>
    <nav class="nav">
      <a class="active">Home</a><a>About Us</a><a>Products</a><a>Our Services</a><a>Contact Us</a>
    </nav>
  </div>
</header>

<section class="hero" role="img" aria-label="Stacked scrap metal and aluminium profiles under dark overlay">
  <div class="hero-inner">
    <h1>WE PROVIDE <em>FULL-SERVICE</em></h1>
    <p>FERROUS AND NON-FERROUS METAL RECYCLER AND PROCESSOR</p>
  </div>
</section>

<section class="about">
  <div class="wrap">
    <div class="about-text">
      <div class="eyebrow">Company</div>
      <h2 class="section-title">About Us</h2>
      <p class="lead">Tovarek Metals Recycling has become a recycling industry leader in the local market</p>
      <p>Tovarek Metals Recycling is a trusted metal recovery partner in Singapore with a track record spanning decades. Through firm commitment to quality and responsible processing we serve a wide range of clients, from individual sellers to large industrial firms, handling aluminium, stainless steel, copper, brass and iron scrap with care, speed and fair pricing on every load.</p>
      <span class="btn">Learn More</span>
    </div>
    <div class="factory-photo" role="img" aria-label="Company factory building with green facade and blue sky"></div>
  </div>
</section>

<section class="services">
  <div class="wrap">
    <div class="eyebrow">What we offer</div>
    <h2 class="section-title">Our Services</h2>
    <div class="services-head">
      <p class="lead">Tovarek Metals Recycling provides one-stop scrap solutions for all levels, from international to corporate to individual</p>
      <span class="btn">View All Services</span>
    </div>
    <div class="cards">
      <article class="card">
        <div class="card-photo" role="img" aria-label="Pile of mixed scrap metal"></div>
        <div class="card-body"><h3>For Individual</h3><p>We accept the general public bringing metal scrap for a fair price. Weighing is done on site and payment is quick and simple.</p><span class="more">See more →</span></div>
      </article>
      <article class="card">
        <div class="card-photo" role="img" aria-label="Sorted aluminium and steel offcuts"></div>
        <div class="card-body"><h3>For Corporate</h3><p>Tovarek Metals provides dependable collection and processing services for businesses of every size and sector.</p><span class="more">See more →</span></div>
      </article>
      <article class="card">
        <div class="card-photo" role="img" aria-label="Copper and brass scrap heap"></div>
        <div class="card-body"><h3>For International</h3><p>Tovarek Metals builds long-lasting ties with overseas partners, offering steady supply and careful grading.</p><span class="more">See more →</span></div>
      </article>
    </div>
  </div>
</section>

<section class="process">
  <div class="wrap">
    <div class="eyebrow">How we work</div>
    <h2 class="section-title">Process</h2>
    <div class="steps">
      <div class="step"><svg viewBox="0 0 54 54"><circle cx="27" cy="27" r="25" fill="#fff" stroke="#e2a31f" stroke-width="2"/><rect x="15" y="22" width="18" height="12" fill="none" stroke="#2b2b2b" stroke-width="2"/><path d="M33 26h5l3 4v4h-8" fill="none" stroke="#2b2b2b" stroke-width="2"/></svg><h4>Procurement &amp; Collection</h4><p>Scrap is collected from homes and companies and delivered safely to our yard for processing.</p></div>
      <div class="step"><svg viewBox="0 0 54 54"><circle cx="27" cy="27" r="25" fill="#fff" stroke="#e2a31f" stroke-width="2"/><path d="M17 20h20M17 27h20M17 34h20" stroke="#2b2b2b" stroke-width="2"/></svg><h4>Sorting &amp; Segregation</h4><p>On arrival, metal is sorted and separated into distinct grades and types.</p></div>
      <div class="step"><svg viewBox="0 0 54 54"><circle cx="27" cy="27" r="25" fill="#fff" stroke="#e2a31f" stroke-width="2"/><path d="M17 28l7 7 13-15" fill="none" stroke="#2b2b2b" stroke-width="2.5"/></svg><h4>Ferrous Scrap</h4><p>Iron and steel are graded and cut to size, then bundled for dispatch to mills.</p></div>
      <div class="step"><svg viewBox="0 0 54 54"><circle cx="27" cy="27" r="25" fill="#fff" stroke="#e2a31f" stroke-width="2"/><circle cx="27" cy="27" r="9" fill="none" stroke="#2b2b2b" stroke-width="2"/></svg><h4>Non-Ferrous Scrap</h4><p>Aluminium, copper and brass are cleaned, graded and packed to meet buyer needs.</p></div>
      <div class="step"><svg viewBox="0 0 54 54"><circle cx="27" cy="27" r="25" fill="#fff" stroke="#e2a31f" stroke-width="2"/><path d="M27 15l10 4v8c0 6-4 10-10 12-6-2-10-6-10-12v-8z" fill="none" stroke="#2b2b2b" stroke-width="2"/></svg><h4>Quality Control</h4><p>Every batch is checked and tested to ensure steady, reliable quality.</p></div>
      <div class="step"><svg viewBox="0 0 54 54"><circle cx="27" cy="27" r="25" fill="#fff" stroke="#e2a31f" stroke-width="2"/><path d="M16 37V22l11-6 11 6v15z" fill="none" stroke="#2b2b2b" stroke-width="2"/></svg><h4>Storage &amp; Sales</h4><p>Sorted stock is stored and sold to local and overseas markets.</p></div>
    </div>
  </div>
</section>

<section class="contact">
  <div class="wrap">
    <div class="head"><div class="eyebrow">Get in touch</div><h2 class="section-title">Please Feel Free To Contact Us</h2></div>
    <div class="contact-body">
      <div class="form">
        <p class="note">Please use the form below to reach us</p>
        <p class="note-2">We'll be in contact with you soon</p>
        <div class="row"><div class="field">Name *</div><div class="field">Company *</div></div>
        <div class="row"><div class="field">Email *</div><div class="field">Contact *</div></div>
        <div class="row"><div class="field msg">Enquiry *</div></div>
        <span class="btn">Send</span>
      </div>
      <div class="map" role="img" aria-label="Map showing the yard location by the waterfront"></div>
    </div>
  </div>
</section>

<footer class="site-footer">
  <div class="wrap">
    <div class="foot-col">
      <div class="brand"><span class="brand-mark"></span><span>TOVAREK METALS<br>RECYCLING</span></div>
      <p>Tovarek Metals Recycling is a scrap metal trader serving Singapore and the region, buying and processing ferrous and non-ferrous metals for reuse.</p>
    </div>
    <div class="foot-col"><h4>Links</h4><ul><li>Home</li><li>About Us</li><li>Products</li><li>Our Services</li><li>Contact Us</li></ul></div>
    <div class="foot-col"><h4>Contact</h4><ul><li>18 Harbour Works Lane,<br>Singapore 700018</li><li>+65 6100 2040</li><li>hello@tovarekmetals.com</li><li>www.tovarekmetals.com</li></ul></div>
    <div class="foot-col"><h4>Business Hours</h4><ul><li>Monday – Friday: 8am – 6pm</li><li>Saturday: 8am – 1pm</li><li>Sunday and Public Holidays: Closed</li></ul></div>
  </div>
  <div class="copyright">© Tovarek Metals Recycling. All rights reserved.</div>
</footer>

</body>
</html>
```